Lumen Peak Website - Enabling Omni channel

Slogan : Enabling Omnichannel Sales

1. Sell products via multiple sale channels
2. Access our technology and services to get your products moving through new channels
3. Customise our mobile and web technology platforms to suit your supply chain.

Slogan: Lumen peak – Innovating new business.

Use the content from these websites to create a new one
http://quorvanthq.com/
http://bralowe-designs.com/lumenPeak02/

Target Market(s)

Business and Coporations who need mobile and web technology or services to increase product sales within their vertical industry. Our case studies show the industries we have worked in; namely: Retail, wholesale, online retail, motor and auto trade. Also have rich experience in Importing and Exporting.

Industry/Entity Type

Retail

Number of Pages Required

3 page

Font styles to use
Sans Serif

Colors
0255a3
ec1f27
9bcb3c
ffffff
0792cd
ffc214

Requirements
Must have
• Punchy headline home page with possible animations or unique and interesting images

```html
<!DOCTYPE html>
<html lang="en">
<head>
<meta charset="utf-8">
<title>Lumen Peak – Innovating New Business</title>
<link rel="stylesheet" href="https://fonts.googleapis.com/css2?family=Raleway:wght@500;600;700;800&family=Open+Sans:ital,wght@0,400;0,600;0,700;1,400&display=swap">
<style>
:root{
  --blue:#0255a3;
  --red:#ec1f27;
  --green:#9bcb3c;
  --white:#ffffff;
  --sky:#0792cd;
  --yellow:#ffc214;
  --ink:#333333;
  --muted:#666666;
  --header:#edf2f8;
  --night:#070b18;
  --footer:#1c1c1d;
}
*{margin:0;padding:0;box-sizing:border-box}
html,body{width:1200px;height:2560px;overflow:hidden}
body{font-family:"Open Sans",Arial,sans-serif;color:var(--ink);background:var(--white);position:relative}
.abs{position:absolute}
.rainbow{position:absolute;left:0;width:1200px;height:5px;display:flex}
.rainbow span{flex:1}
.rainbow span:nth-child(1){background:var(--sky)}
.rainbow span:nth-child(2){background:var(--yellow)}
.rainbow span:nth-child(3){background:var(--green)}
.rainbow span:nth-child(4){background:var(--red)}

/* header */
.site-header{position:absolute;top:0;left:0;width:1200px;height:97px;background:var(--header)}
.brand{position:absolute;left:162px;top:26px}
.brand-name{font-family:"Raleway",sans-serif;font-weight:800;font-size:30px;color:var(--blue);display:flex;align-items:center;gap:8px;line-height:1}
.brand-name i{display:block;width:14px;height:14px;border-radius:50%;background:var(--sky)}
.brand-tag{font-family:"Raleway",sans-serif;font-weight:600;font-size:13px;color:#222;margin:4px 0 0 22px}
.call{position:absolute;right:162px;top:20px;font-family:"Raleway",sans-serif;font-weight:700;font-size:17px;color:var(--red)}
.nav{position:absolute;right:162px;top:66px;display:flex;gap:34px;list-style:none;font-family:"Raleway",sans-serif;font-weight:700;font-size:12.5px;color:#222}
.nav .active{color:var(--green)}

/* hero */
.hero{position:absolute;top:97px;left:0;width:1200px;height:487px;background:radial-gradient(circle at 30% 45%,#1d3a66 0%,#0b1530 35%,var(--night) 70%)}
.hero-art{position:absolute;left:110px;top:20px;width:420px;height:450px;border-radius:50%;background:radial-gradient(circle at 50% 45%,rgba(255,225,170,.55) 0%,rgba(40,150,210,.45) 30%,rgba(10,30,70,0) 70%)}
.hero-text{position:absolute;right:162px;top:140px;width:430px;text-align:right}
.hero-text h1{font-family:"Raleway",sans-serif;font-weight:600;font-size:41px;color:var(--white);line-height:1.2}
.hero-text h2{font-family:"Raleway",sans-serif;font-weight:600;font-size:32px;color:var(--green);margin-top:8px;line-height:1.2}
.hero-text p{font-size:11px;line-height:19px;color:#e8e8e8;margin-top:14px}
.arrow{position:absolute;top:210px}
.dots{position:absolute;display:flex;gap:6px}
.dots span{width:11px;height:11px;border-radius:50%;background:var(--white)}
.dots .on{background:var(--green)}

/* solutions */
.section-title{font-family:"Raleway",sans-serif;font-weight:700;font-size:22px;color:#333;text-align:center;letter-spacing:.3px}
.solutions{position:absolute;top:584px;left:0;width:1200px;height:338px}
.solutions .section-title{position:absolute;top:36px;width:100%}
.solution{position:absolute;top:88px;width:200px;text-align:center}
.solution .ring{width:96px;height:96px;border-radius:50%;margin:0 auto;border:3px solid;padding:4px}
.solution .disc{width:100%;height:100%;border-radius:50%;display:flex;align-items:center;justify-content:center}
.solution h3{font-family:"Raleway",sans-serif;font-weight:600;font-size:15px;color:#222;margin-top:18px}
.solution p{font-size:11px;line-height:18px;color:#444;margin-top:10px}
.small-dots{position:absolute;top:299px;left:578px;display:flex;gap:3px}
.small-dots span{width:9px;height:9px;border-radius:50%;background:#888}
.small-dots .on{background:var(--green)}

/* marketing band */
.marketing{position:absolute;top:922px;left:0;width:1200px;height:333px;background:linear-gradient(90deg,#f2b51a,var(--yellow) 60%,#f6bb1a)}
.laptop{position:absolute;left:162px;top:65px;width:322px;height:203px}
.laptop .screen{position:absolute;left:20px;top:0;width:282px;height:190px;background:#1b1b1b;border-radius:8px;padding:10px}
.laptop .screen div{width:100%;height:100%;background:linear-gradient(135deg,#f4f4f4,#dfe6ea)}
.laptop .base{position:absolute;left:0;top:189px;width:322px;height:12px;background:linear-gradient(#e4e4e4,#a9a9a9);border-radius:0 0 12px 12px}
.marketing-copy{position:absolute;left:589px;top:70px;width:450px}
.marketing-copy h2{font-family:"Raleway",sans-serif;font-weight:700;font-size:23px;color:var(--white)}
.marketing-copy h3{font-family:"Raleway",sans-serif;font-weight:700;font-size:15px;color:var(--white);margin-top:3px}
.marketing-copy p{font-size:11px;line-height:19px;color:#fff6dc;margin-top:12px}
.btn{display:inline-block;font-family:"Raleway",sans-serif;font-weight:700;font-size:11.5px;color:var(--white);text-align:center;border-radius:20px}
.btn-red{background:var(--red);width:140px;height:38px;line-height:38px;margin-top:18px}

/* offer cards */
.offers{position:absolute;top:1255px;left:0;width:1200px;height:440px}
.offer{position:absolute;top:37px;width:271px}
.offer .photo{width:100%;height:181px}
.offer h3{font-family:"Raleway",sans-serif;font-weight:700;font-size:17px;color:#333;margin-top:22px}
.offer p{font-size:11px;line-height:19px;color:#444;margin-top:14px;width:265px}
.btn-green{background:var(--green);width:109px;height:35px;line-height:35px;margin-top:18px;font-size:10.5px}

/* success stories */
.stories{position:absolute;top:1695px;left:0;width:1200px;height:260px;background:var(--green)}
.stories .section-title{position:absolute;top:54px;width:100%;color:var(--white)}
.avatar{position:absolute;left:190px;top:101px;width:90px;height:90px;border-radius:50%;border:4px solid var(--white);background:linear-gradient(#d8e4ef,#a9b9c9)}
.quote-badge{position:absolute;left:256px;top:157px;width:30px;height:30px;border-radius:50%;background:var(--red);border:2px solid var(--white)}
.story-text{position:absolute;left:311px;top:112px;width:730px;font-style:italic;font-size:11.5px;line-height:20px;color:var(--white)}
.story-name{position:absolute;left:311px;top:180px;font-family:"Raleway",sans-serif;font-weight:700;font-size:12.5px;color:var(--white)}

/* reach */
.reach{position:absolute;top:1955px;left:0;width:1200px;height:338px}
.reach h2{position:absolute;left:162px;top:44px;width:490px;font-family:"Raleway",sans-serif;font-weight:700;font-size:19px;line-height:26px;color:#333}
.reach ul{position:absolute;left:162px;top:146px;list-style:none}
.reach li{font-size:11px;line-height:20.5px;color:#333;display:flex;align-items:center;gap:9px}
.reach li svg{flex:none}
.store{position:absolute;left:162px;top:268px;display:flex;align-items:center;gap:10px;font-family:"Raleway",sans-serif;font-weight:700;font-size:17px;color:#111}
.store .sep{width:1px;height:22px;background:#999}
.store .name{color:var(--blue)}
.shoppers{position:absolute;left:800px;top:10px;width:245px;height:290px;background:radial-gradient(ellipse at 50% 55%,#f2d6d8 0%,#f7e9ea 45%,rgba(255,255,255,0) 72%)}

/* footer */
.site-footer{position:absolute;top:2296px;left:0;width:1200px;height:264px;background:var(--footer);color:#ddd}
.foot-brand{position:absolute;left:162px;top:60px;font-family:"Raleway",sans-serif;font-weight:800;font-size:28px;color:#bdbdbd;display:flex;align-items:center;gap:8px}
.foot-brand i{display:block;width:12px;height:12px;border-radius:50%;background:#bdbdbd}
.social{position:absolute;left:162px;top:126px;display:flex;gap:9px}
.social span{width:30px;height:30px;border-radius:50%;border:1.5px solid #aaa}
.foot-col{position:absolute;top:42px}
.foot-col h4{font-family:"Raleway",sans-serif;font-weight:700;font-size:13.5px;color:var(--white);margin-bottom:10px;letter-spacing:.3px}
.foot-col li{list-style:none;font-size:10.5px;line-height:19px;color:#e4e4e4}
.foot-col p{font-size:10.5px;line-height:19px;color:#e4e4e4}
.newsletter{display:flex;margin-top:14px}
.newsletter .field{width:215px;height:40px;background:var(--white);font-size:10.5px;color:#999;padding:0 12px;line-height:40px}
.newsletter .submit{width:80px;height:40px;background:var(--green);color:var(--white);font-family:"Raleway",sans-serif;font-weight:700;font-size:12px;line-height:40px;text-align:center}
.copyright{position:absolute;top:228px;left:0;width:1200px;text-align:center;font-size:10px;color:#cfcfcf}
</style>
</head>
<body>

<div class="rainbow" style="top:0"><span></span><span></span><span></span><span></span></div>

<header class="site-header" style="top:5px;height:92px">
  <div class="brand" style="top:22px">
    <div class="brand-name"><i></i>Lumen Peak</div>
    <div class="brand-tag">Innovating New Business</div>
  </div>
  <div class="call" style="top:15px">CALL US:071-455-2068</div>
  <ul class="nav" style="top:61px">
    <li class="active">HOME</li><li>ABOUT US</li><li>WHY US..?</li><li>CASE STUDIES</li><li>FAQS</li><li>CONTACT</li>
  </ul>
</header>

<section class="hero">
  <div class="hero-art" role="img" aria-label="Hand reaching toward glowing floating blue cubes over a dark network backdrop"></div>
  <div class="hero-text">
    <h1>Lumen Peak.</h1>
    <h2>Innovating New Business</h2>
    <p>Sed ut perspiciatis unde omnis iste natus error sit voluptatem accusantium dolo remque laudantium, totam rem aperiam, eaque ipsa quae ab illo inventore veritatis et quasi architecto beatae vitae dicta sunt explicabo. Nemo enim ipsam voluptatem quia voluptas sit atae vitae dicta sunt explicaemo enim spernatur aut o</p>
  </div>
  <svg class="arrow" style="left:20px" width="34" height="72" viewBox="0 0 34 72"><polyline points="32,2 2,36 32,70" fill="none" stroke="#ffffff" stroke-opacity=".7" stroke-width="2"/></svg>
  <svg class="arrow" style="right:20px" width="34" height="72" viewBox="0 0 34 72"><polyline points="2,2 32,36 2,70" fill="none" stroke="#ffffff" stroke-opacity=".7" stroke-width="2"/></svg>
  <div class="dots" style="left:564px;top:428px"><span></span><span></span><span></span><span class="on"></span><span></span></div>
</section>

<section class="solutions">
  <h2 class="section-title">OUR SOLUTIONS</h2>
  <div class="solution" style="left:151px">
    <div class="ring" style="border-color:var(--green)"><div class="disc" style="background:var(--green)">
      <svg width="40" height="40" viewBox="0 0 40 40"><circle cx="20" cy="13" r="8" fill="#fff"/><path d="M5 37c0-9 7-14 15-14s15 5 15 14z" fill="#fff"/></svg>
    </div></div>
    <h3>Customer Service</h3>
    <p>Sed ut perspiciatis unde omnis iste natus error sit voluptatem accntium doloremque laudantiutotam.</p>
  </div>
  <div class="solution" style="left:383px">
    <div class="ring" style="border-color:var(--red)"><div class="disc" style="background:var(--red)">
      <svg width="40" height="40" viewBox="0 0 40 40"><path d="M10 36v-8c-4-3-6-7-5-12 1-7 7-12 14-12 8 0 14 6 14 13l3 6h-4v5c0 2-2 3-4 3h-4v5z" fill="#fff"/><circle cx="19" cy="16" r="5" fill="var(--red)"/></svg>
    </div></div>
    <h3>Business intelligence</h3>
    <p>Sed ut perspiciatis unde omnis iste natus error sit voluptatem accntium doloremque laudantiutotam.</p>
  </div>
  <div class="solution" style="left:615px">
    <div class="ring" style="border-color:var(--sky)"><div class="disc" style="background:var(--sky)">
      <svg width="40" height="40" viewBox="0 0 40 40"><rect x="20" y="4" width="16" height="11" rx="1" fill="#fff"/><circle cx="15" cy="14" r="6" fill="#fff"/><path d="M4 37c0-8 5-13 11-13s11 5 11 13z" fill="#fff"/></svg>
    </div></div>
    <h3>Advice and consulting</h3>
    <p>Sed ut perspiciatis unde omnis iste natus error sit voluptatem accntium doloremque laudantiutotam.</p>
  </div>
  <div class="solution" style="left:847px">
    <div class="ring" style="border-color:var(--yellow)"><div class="disc" style="background:var(--yellow)">
      <svg width="42" height="40" viewBox="0 0 42 40"><path d="M3 16 21 6l18 10v20H3z" fill="#fff"/><rect x="10" y="20" width="9" height="7" fill="var(--yellow)"/><rect x="23" y="20" width="9" height="7" fill="var(--yellow)"/><rect x="16" y="29" width="9" height="7" fill="var(--yellow)"/></svg>
    </div></div>
    <h3>Warehouse services</h3>
    <p>Sed ut perspiciatis unde omnis iste natus error sit voluptatem accntium doloremque laudantiutotam.</p>
  </div>
  <div class="small-dots"><span></span><span class="on"></span><span></span><span></span></div>
</section>

<section class="marketing">
  <div class="laptop">
    <div class="screen"><div role="img" aria-label="Marketing plan sketch with doodled charts and icons on the laptop screen"></div></div>
    <div class="base"></div>
  </div>
  <div class="marketing-copy">
    <h2>MARKETING AND SALES</h2>
    <h3>We go to the ends of the earth to get your products selling.</h3>
    <p>Sed ut perspiciatis unde omnis iste natus error sit voluptatem accusantium doloremque laudantium, totam rem aperiam, eaque ipsa quae ab illo inventore veritatis et quasi architecto beatae vitae dicta sunt explicabo. Nemo enim ipsam voluptatem quia voluptas sit aspernatur aut odit aut fugit, sed quia consequuntur magni dolores.</p>
    <span class="btn btn-red">READ MORE</span>
  </div>
</section>

<section class="offers">
  <article class="offer" style="left:162px">
    <div class="photo" role="img" aria-label="Glowing cube among dark blue blocks" style="background:linear-gradient(135deg,#3a5a8c,#1c2a4a 55%,#c9a27a)"></div>
    <h3>ARE YOU A BRAND</h3>
    <p>Sed ut perspiciatis unde omnis iste natus error sit voluptatem accusantium doloremque laudantium, totam rem aperiam, eaque ipsa quae ab illo invent ore veritatis et quasi architecto beatae vitae.</p>
    <span class="btn btn-green">READ MORE</span>
  </article>
  <article class="offer" style="left:461px">
    <div class="photo" role="img" aria-label="Shop owner standing in a coffee roastery" style="background:linear-gradient(135deg,#5b5e66,#2f2c2c 50%,#7a6552)"></div>
    <h3>DO YOU HAVE PRODUCTS</h3>
    <p>Sed ut perspiciatis unde omnis iste natus error sit voluptatem accusantium doloremque laudantium, totam rem aperiam, eaque ipsa quae ab illo invent ore veritatis et quasi architecto beatae vitae.</p>
    <span class="btn btn-green">READ MORE</span>
  </article>
  <article class="offer" style="left:768px">
    <div class="photo" role="img" aria-label="Warehouse manager with clipboard beside stacked cartons" style="background:linear-gradient(135deg,#8c6b4c,#c7a27a 50%,#6d5642)"></div>
    <h3>DO YOU OFFER A SERVICE?</h3>
    <p>Sed ut perspiciatis unde omnis iste natus error sit voluptatem accusantium doloremque laudantium, totam rem aperiam, eaque ipsa quae ab illo invent ore veritatis et quasi architecto beatae vitae.</p>
    <span class="btn btn-green">READ MORE</span>
  </article>
</section>

<section class="stories">
  <h2 class="section-title">SUCCESS STORIES</h2>
  <div class="avatar" role="img" aria-label="Client portrait"></div>
  <div class="quote-badge"></div>
  <p class="story-text">Sed ut perspiciatis unde omnis iste nloreatus error sit volupt atem accusantiuloremm dol ore mq ue laudantiumtota m rem aperiam, eaque ipsa quae ab illo inventore ver itatis et asi architecto beatae vita sit aspernatued ut perspiciatis unde omnis iste nloreatus error sit volupt atem accusantium dolorem que laudantiumtota m rem aperi ue ipsa qu ae ab illo inventore ver itatis et quasi</p>
  <div class="story-name">Dana Verrow, City Name</div>
</section>

<section class="reach">
  <h2>WE CAN POSITION YOUR PRODUCTS, SERVICES AND BRAND IN FRONT OF MILLIONS OF NEW ONLINE CUSTOMERS, WHICH WILL:</h2>
  <ul>
    <li><svg width="10" height="10" viewBox="0 0 10 10"><circle cx="5" cy="5" r="5" fill="var(--green)"/><polyline points="4,3 6,5 4,7" fill="none" stroke="#fff" stroke-width="1.3"/></svg>Drive more traffic to your online and offline retail stores</li>
    <li><svg width="10" height="10" viewBox="0 0 10 10"><circle cx="5" cy="5" r="5" fill="var(--green)"/><polyline points="4,3 6,5 4,7" fill="none" stroke="#fff" stroke-width="1.3"/></svg>Increase your brand awareness</li>
    <li><svg width="10" height="10" viewBox="0 0 10 10"><circle cx="5" cy="5" r="5" fill="var(--green)"/><polyline points="4,3 6,5 4,7" fill="none" stroke="#fff" stroke-width="1.3"/></svg>Revolutionise your ancillary sales and per-customer transactional values</li>
    <li><svg width="10" height="10" viewBox="0 0 10 10"><circle cx="5" cy="5" r="5" fill="var(--green)"/><polyline points="4,3 6,5 4,7" fill="none" stroke="#fff" stroke-width="1.3"/></svg>Launch your new service and product lines</li>
    <li><svg width="10" height="10" viewBox="0 0 10 10"><circle cx="5" cy="5" r="5" fill="var(--green)"/><polyline points="4,3 6,5 4,7" fill="none" stroke="#fff" stroke-width="1.3"/></svg>Quickly clear your excess and discontinued stock</li>
  </ul>
  <div class="store"><span>Visit our Online Store</span><span class="sep"></span><span class="name">Vendora</span></div>
  <div class="shoppers" role="img" aria-label="Illustration of three women carrying shopping bags"></div>
</section>

<div class="rainbow" style="top:2291px"><span></span><span></span><span></span><span></span></div>

<footer class="site-footer">
  <div class="foot-brand"><i></i>Lumen Peak</div>
  <div class="social"><span></span><span></span><span></span><span></span></div>
  <div class="foot-col" style="left:398px">
    <h4>ABOUT</h4>
    <ul><li>Home</li><li>About Us</li><li>Why Us..?</li><li>Case Studies</li><li>FAQs</li><li>Contact</li></ul>
  </div>
  <div class="foot-col" style="left:529px">
    <h4>CONTACT INFO</h4>
    <p>+61 2 7140 6628<br>hello@lumenpeak.example<br>12 Orrin Lane, 7 Westvale,<br>&nbsp;Port Kellan, USA</p>
  </div>
  <div class="foot-col" style="left:744px;width:300px">
    <h4>NEWSLETTER SIGN UP</h4>
    <p>Sut perspiciatis unde omnis iste natus error sit voluptatem accusciatis unde omnis ist.</p>
    <div class="newsletter"><div class="field">Email Address:</div><div class="submit">SUBMIT</div></div>
  </div>
  <div class="copyright">© 2016 All Copyright are reserved, Terms and Conditions.Lumen Peak.</div>
</footer>

</body>
</html>
```